Construction Trailer Wrap Design

Create a visually stunning but simple graphic design for our Construction trailers. We are in the Construction business.

Info to have on the trailer:

Commercial & Residential Roofing
Exterior & Interior Renovations
General Contracting
Custom Builds

519-430-7182
www.brindlecrestbuilds.ca

Target Market(s)

Home Owners

Industry/Entity Type

Residential Construction

Colors
f78f20
ffffff
1b1b1b

Requirements
Must have
• Info to have on the trailer: Brindlecrest Group Logo & QTA Logo
• Commercial & Residential Roofing
• Exterior & Interior Renovations
• General Contracting
• 519-430-7182
• www.brindlecrestbuilds.ca
• Business Licensee #371905268

```html
<!DOCTYPE html>
<html lang="en">
<head>
<meta charset="utf-8">
<title>Brindlecrest Group – Trailer Wrap</title>
<link rel="stylesheet" href="https://fonts.googleapis.com/css2?family=Oswald:wght@500;600;700&family=Montserrat:wght@600;700&family=Exo+2:ital,wght@1,800;1,900&display=swap">
<style>
  :root {
    --orange: #f78f20;
    --orange-deep: #e2661c;
    --white: #ffffff;
    --ink: #1b1b1b;
    --steel-light: #f3f3f3;
    --steel-mid: #c9c9cb;
    --steel-dark: #9fa0a4;
    --stage: #e4e4e4;
  }
  * { margin: 0; padding: 0; box-sizing: border-box; }
  html, body {
    width: 1200px; height: 938px; overflow: hidden;
    background: var(--stage);
  }
  .wrap {
    position: absolute; left: 30px; top: 178px;
    width: 1140px; height: 582px;
    overflow: hidden;
    border: 2px solid #b5b5b8;
  }
  .wrap-art { position: absolute; inset: 0; width: 100%; height: 100%; }

  .license {
    position: absolute; left: 28px; top: 22px;
    display: flex; align-items: center; gap: 34px;
  }
  .license-badge {
    width: 46px; height: 72px; border-radius: 3px;
    background: var(--white);
  }
  .license-text {
    font-family: "Montserrat", sans-serif; font-weight: 600;
    color: var(--white); font-size: 16px; line-height: 1.3;
  }

  .services-title {
    position: absolute; left: 118px; top: 126px;
    font-family: "Oswald", sans-serif; font-weight: 700;
    font-size: 48px; letter-spacing: -0.5px; line-height: 1;
    color: var(--ink);
    -webkit-text-stroke: 6px var(--white); paint-order: stroke fill;
    text-shadow: 1px 2px 3px rgba(0,0,0,.35);
  }
  .services-list { position: absolute; left: 22px; top: 196px; list-style: none; }
  .service {
    display: flex; align-items: center; gap: 12px;
    height: 42px;
    font-family: "Oswald", sans-serif; font-weight: 500;
    font-size: 26px; letter-spacing: -0.4px; color: var(--ink);
    white-space: nowrap;
  }
  .service svg { width: 28px; height: 28px; flex: none; }

  .phone {
    position: absolute; left: 38px; top: 388px;
    font-family: "Exo 2", sans-serif; font-style: italic; font-weight: 900;
    font-size: 60px; letter-spacing: -1px; line-height: 1;
    color: var(--orange-deep);
    -webkit-text-stroke: 7px var(--white); paint-order: stroke fill;
    text-shadow: 3px 3px 2px rgba(0,0,0,.55);
  }
  .call-cta {
    position: absolute; left: 36px; top: 460px;
    font-family: "Exo 2", sans-serif; font-style: italic; font-weight: 800;
    font-size: 34px; line-height: 1; letter-spacing: 0.5px;
    color: var(--white);
    -webkit-text-stroke: 4px var(--ink); paint-order: stroke fill;
  }

  .web-band {
    position: absolute; left: 500px; top: 400px;
    width: 600px; height: 41px;
    background: linear-gradient(90deg, var(--orange-deep), var(--orange) 60%, var(--orange-deep));
  }
  .web-url {
    position: absolute; right: 18px; top: 2px;
    font-family: "Montserrat", sans-serif; font-weight: 700;
    font-size: 30px; line-height: 36px; color: var(--white);
    text-shadow: 1px 1px 2px rgba(0,0,0,.4);
  }

  .brand {
    position: absolute; left: 500px; top: 50px;
    width: 330px; height: 330px; border-radius: 50%;
    background: var(--white);
    border: 10px solid var(--ink);
    display: flex; align-items: center; justify-content: center; text-align: center;
  }
  .brand-name {
    font-family: "Oswald", sans-serif; font-weight: 700;
    font-size: 40px; line-height: 1.05; color: var(--orange-deep);
    text-transform: uppercase;
  }
</style>
</head>
<body>
  <div class="wrap">
    <svg class="wrap-art" viewBox="0 0 1140 582" preserveAspectRatio="none">
      <defs>
        <linearGradient id="steel" x1="0" y1="0" x2="1" y2="0">
          <stop offset="0" stop-color="#d8d8da"/>
          <stop offset=".35" stop-color="#f3f3f3"/>
          <stop offset="1" stop-color="#9fa0a4"/>
        </linearGradient>
        <linearGradient id="scene" x1="0" y1="0" x2="1" y2="0">
          <stop offset="0" stop-color="#b4b2bc" stop-opacity="0"/>
          <stop offset=".35" stop-color="#a9a7b8" stop-opacity=".8"/>
          <stop offset="1" stop-color="#5d6376"/>
        </linearGradient>
      </defs>
      <rect width="1140" height="582" fill="url(#steel)"/>
      <rect x="403" y="20" width="721" height="435" fill="url(#scene)" role="img" aria-label="Photo of a two-storey suburban house with grey siding, lit windows and a wet driveway at dusk"/>
      <path d="M0 0 H1140 V16 C900 18 560 26 300 70 C180 92 80 120 0 140 Z" fill="#1b1b1b"/>
      <path d="M0 150 C240 86 540 44 820 34 C560 52 260 100 0 176 Z" fill="#f78f20"/>
      <path d="M0 582 V540 C360 546 720 510 1140 440 V582 Z" fill="#1b1b1b"/>
      <path d="M560 526 C800 482 1000 456 1140 428 V440 C1000 466 800 496 560 526 Z" fill="#f78f20"/>
      <path d="M0 536 H420 V539 H0 Z" fill="#f78f20"/>
    </svg>

    <div class="license">
      <div class="license-badge" aria-hidden="true"></div>
      <p class="license-text">Business Licensee<br>#371905268</p>
    </div>

    <h2 class="services-title">OUR SERVICES</h2>
    <ul class="services-list">
      <li class="service"><svg viewBox="0 0 30 30"><rect x="2" y="6" width="22" height="22" rx="3" fill="none" stroke="#1b1b1b" stroke-width="2.5"/><path d="M7 16 L13 22 L28 4" fill="none" stroke="#f78f20" stroke-width="4" stroke-linecap="round" stroke-linejoin="round"/></svg>COMMERCIAL &amp; RESIDENTIAL ROOFING</li>
      <li class="service"><svg viewBox="0 0 30 30"><rect x="2" y="6" width="22" height="22" rx="3" fill="none" stroke="#1b1b1b" stroke-width="2.5"/><path d="M7 16 L13 22 L28 4" fill="none" stroke="#f78f20" stroke-width="4" stroke-linecap="round" stroke-linejoin="round"/></svg>EXTERIOR &amp; INTERIOR RENOVATIONS</li>
      <li class="service"><svg viewBox="0 0 30 30"><rect x="2" y="6" width="22" height="22" rx="3" fill="none" stroke="#1b1b1b" stroke-width="2.5"/><path d="M7 16 L13 22 L28 4" fill="none" stroke="#f78f20" stroke-width="4" stroke-linecap="round" stroke-linejoin="round"/></svg>GENERAL CONTRACTING</li>
      <li class="service"><svg viewBox="0 0 30 30"><rect x="2" y="6" width="22" height="22" rx="3" fill="none" stroke="#1b1b1b" stroke-width="2.5"/><path d="M7 16 L13 22 L28 4" fill="none" stroke="#f78f20" stroke-width="4" stroke-linecap="round" stroke-linejoin="round"/></svg>CUSTOM BUILDS</li>
    </ul>

    <div class="web-band"><span class="web-url">www.brindlecrestbuilds.ca</span></div>

    <p class="phone">519-430-7182</p>
    <p class="call-cta">CALL US TODAY</p>

    <div class="brand"><span class="brand-name">Brindlecrest<br>Group Inc.</span></div>
  </div>
</body>
</html>
```